CD Cover Design Project - Illustrated cover

I need a cd cover design for a new music album I am recording.

FRONT COVER:

I am not asking for a photo-montage of all the photographs provided, but an illustrated drawing. All the photographs have been attached for your reference.

I'd like the front cover to be an illustration of me playing guitar and singing into a microphone on the street in Covent Garden. The illustration should have the floor made up of cobbles (see Image 1) and I'd like the building in the background to be the same as Image 2. Please keep 'Ashbury Row Market' written on the building, but remove 'Fox & Lark'.

I've attached a photo of me playing guitar (Image 3) for reference.

I'd like to be illustrated wearing a dress. If you plan on showing shoes, then I'd like boots (cowgirl, etc)- my style is kind of country-chic.

I have also included a close-up of my face (Image 5). The photo is black and white so for reference, my hair is dark blonde and my eyes are hazel.

PLEASE NOTE: This black and white image is for REFERENCE ONLY. Please do not include this image on the cover as it is already being used as an album cover for my first album. It is being provided simply so you have a close up of my face and know what I look like for the drawing.

Please include my name Mabel Trent somewhere in a prominent position.

BACK COVER:

Please make the background plain and in whatever colour you think matches the colour scheme of your front cover.

The back cover should take the following format:

List of songs in this order:

Velvet Orchard
Bring the Lantern In
Hollow Tin Kettle
Row Your Skiff at Dusk
The Pale Gate
Wait Beside Tamarind
Fold a Letter
Whistling Past the Granary

www.MabelTrent.co.uk

Hi everyone, the deadline has been extended by another 5 days. Please also take another look at the brief, as I have updated it with some extra information.

Target Market(s)

I am a street performer in London's Covent Garden and my customers are made up of locals and tourists walking around the area.

Industry/Entity Type

Building

Requirements
Must have
• This cover must be an illustration / drawing.

The guitar must be acoustic.

Should not have
• The black and white photo of my face should not be used anywhere in the design. This image has been provided for reference only so you know how to draw my face.

Please do no super-impose my head from the image of me playing guitar onto the image of the dress- The angles and proportions do not match well between the two.

```html
<!DOCTYPE html>
<html lang="en">
<head>
<meta charset="utf-8">
<title>Mabel Trent – Back Cover</title>
<link rel="stylesheet" href="https://fonts.googleapis.com/css2?family=Great+Vibes&display=swap">
<style>
  :root {
    --edge-dark: #3a0716;
    --frame-line: #c41a55;
    --field-centre: #f01a78;
    --field-mid: #d4145c;
    --field-edge: #a60e3e;
    --band-tone: #b5164c;
    --number-ink: #7c0d2f;
    --title-ink: #6e0d30;
    --track-ink: #ffffff;
    --ornament-tone: #7c0d2f;
  }
  html, body {
    margin: 0;
    padding: 0;
    width: 1200px;
    height: 1200px;
    overflow: hidden;
    background: var(--edge-dark);
  }
  .back-cover {
    position: relative;
    width: 1200px;
    height: 1200px;
    background: radial-gradient(circle at 50% 55%, var(--field-centre) 0%, var(--field-mid) 45%, var(--field-edge) 80%, var(--edge-dark) 100%);
    font-family: "Great Vibes", cursive;
    overflow: hidden;
  }
  .outer-frame {
    position: absolute;
    inset: 0;
    border: 14px solid var(--edge-dark);
    box-shadow: inset 0 0 0 22px rgba(142, 15, 54, 0.55);
  }
  .inner-frame {
    position: absolute;
    inset: 38px;
    border: 3px solid var(--frame-line);
    opacity: 0.7;
  }
  .pattern-band {
    position: absolute;
    left: 40px;
    right: 40px;
    height: 34px;
    background: var(--band-tone);
    opacity: 0.6;
  }
  .pattern-band.top { top: 48px; }
  .pattern-band.bottom { bottom: 48px; }
  .artist-name {
    position: absolute;
    top: 210px;
    left: 0;
    right: 0;
    margin: 0;
    text-align: center;
    font-weight: 400;
    font-size: 84px;
    line-height: 100px;
    color: var(--title-ink);
  }
  .track-list {
    position: absolute;
    top: 400px;
    left: 0;
    right: 0;
    margin: 0;
    padding: 0;
    list-style: none;
    text-align: center;
  }
  .track {
    font-size: 60px;
    line-height: 60px;
    height: 60px;
    color: var(--track-ink);
    white-space: nowrap;
  }
  .track-number {
    color: var(--number-ink);
    font-size: 66px;
    margin-right: 22px;
  }
  .flourish {
    position: absolute;
    left: 455px;
    top: 950px;
    width: 290px;
    height: 80px;
    background: radial-gradient(ellipse at 50% 50%, var(--ornament-tone) 0%, rgba(124, 13, 47, 0.5) 55%, rgba(124, 13, 47, 0) 75%);
  }
  .website {
    position: absolute;
    top: 1036px;
    left: 0;
    right: 0;
    margin: 0;
    text-align: center;
    font-size: 36px;
    line-height: 40px;
    color: var(--track-ink);
  }
</style>
</head>
<body>
  <main class="back-cover">
    <div class="outer-frame"></div>
    <div class="inner-frame"></div>
    <div class="pattern-band top" role="img" aria-label="Decorative lace pattern band"></div>
    <div class="pattern-band bottom" role="img" aria-label="Decorative lace pattern band"></div>

    <h1 class="artist-name">Mabel Trent</h1>

    <ol class="track-list">
      <li class="track"><span class="track-number">1.</span>Velvet Orchard</li>
      <li class="track"><span class="track-number">2.</span>Bring the Lantern In</li>
      <li class="track"><span class="track-number">3.</span>Hollow Tin Kettle</li>
      <li class="track"><span class="track-number">4.</span>Row Your Skiff at Dusk</li>
      <li class="track"><span class="track-number">5.</span>The Pale Gate</li>
      <li class="track"><span class="track-number">6.</span>Wait Beside Tamarind</li>
      <li class="track"><span class="track-number">7.</span>Fold a Letter</li>
      <li class="track"><span class="track-number">8.</span>Whistling Past the Granary</li>
    </ol>

    <div class="flourish" role="img" aria-label="Decorative scroll flourish ornament"></div>

    <p class="website">www.MabelTrent.co.uk</p>
  </main>
</body>
</html>
```